MARVELTRUST web-presence redisign

We would like to have our existing web-presence redesigned. Have a look at www.pelbrika-example.ch (please use explorer). To the existing 11 pages we would add one more.

```html
<!DOCTYPE html>
<html lang="de">
<head>
<meta charset="utf-8">
<title>MARVELTRUST Zahnarztpraxis</title>
<link rel="stylesheet" href="https://fonts.googleapis.com/css2?family=Open+Sans:wght@400;600;700&family=Anton&display=swap">
<style>
:root{
  --dark:#2b2b2b;
  --darker:#1c1c1c;
  --blue:#3cb3e0;
  --blue-deep:#2494c4;
  --header-bg:#efefef;
  --welcome-bg:#ebebeb;
  --testi-bg:#f4f3f4;
  --gold:#e8a317;
  --gold-dark:#c9850a;
  --text:#222;
  --muted:#cfcfcf;
}
*{box-sizing:border-box;margin:0;padding:0}
html,body{width:785px;height:1200px;overflow:hidden}
body{position:relative;background:var(--welcome-bg);font-family:'Open Sans',sans-serif;color:var(--text)}
.abs{position:absolute}

/* top bar */
.topbar{left:0;top:0;width:785px;height:27px;background:var(--dark);font-size:8.5px;color:#aaa}
.topbar .item{position:absolute;top:9px}
.topbar .home{left:285px;color:var(--gold);font-weight:600}
.topbar .lang{left:359px;color:#ddd}
.topbar .lang span{color:#999}
.topbar .help{left:551px;color:#ddd}
.search{left:603px;top:0;width:165px;height:27px;background:#555;color:#ddd;font-size:8px;padding:12px 9px}

.header{left:0;top:27px;width:785px;height:63px;background:var(--header-bg)}
.brand{left:26px;top:37px;display:flex;align-items:center;gap:8px}
.brand .mark{width:22px;height:22px;background:var(--gold);border-radius:50%}
.brand .name{font-weight:700;font-size:21px;color:var(--gold-dark);letter-spacing:.5px}
.callout{left:346px;top:34px}
.callout .lead{font-size:13px;color:var(--blue-deep);font-weight:600}
.callout .phone{font-size:13px;font-weight:600;color:#222;margin-top:1px}
.phone-icon{left:349px;top:37px}
.socialbox{left:603px;top:27px;width:162px;height:40px;background:#fff;border-radius:0 0 6px 6px;box-shadow:0 1px 3px rgba(0,0,0,.25);display:flex;gap:6px;padding:6px 0 0 28px}
.socialbox i{display:block;width:25px;height:25px;border-radius:5px;background:var(--blue-deep)}
.rule{left:0;top:90px;width:785px;height:4px;background:var(--dark)}
.band{left:0;top:94px;width:785px;height:266px;background:var(--blue-deep)}

/* nav */
.nav{left:70px;top:78px;width:656px;height:29px;background:var(--blue);display:flex;font-size:10px;color:#fff;box-shadow:0 3px 6px rgba(0,0,0,.25)}
.nav a{display:block;padding:9px 0;text-align:center}
.nav .on{background:var(--blue-deep)}
.dropdown{left:227px;top:109px;width:157px;background:#333;font-size:10px;color:#eee;z-index:3}
.dropdown div{height:26px;padding:6px 9px}
.dropdown .on{background:var(--blue)}

/* slider */
.slider{left:24px;top:125px;width:743px;height:270px;background:linear-gradient(100deg,#cfe6f3 0%,#9dc6e6 35%,#e9eef2 60%,#f1c8b5 78%,#e8a590 100%);box-shadow:0 6px 8px rgba(0,0,0,.25)}
.cap1{left:24px;top:284px;width:429px;height:32px;background:rgba(40,40,40,.92);color:#fff;font-size:19px;padding:3px 20px;white-space:nowrap}
.cap2{left:24px;top:329px;width:246px;height:32px;background:#fff;color:#111;font-size:19px;padding:3px 20px}
.cap1 em,.cap2 em{font-style:normal;color:var(--blue)}
.arrow{top:215px}

/* thumbs */
.thumb{top:416px;width:208px;height:136px;background:#fff;border:2px solid #111;padding:3px;box-shadow:0 8px 6px -4px rgba(0,0,0,.35)}
.thumb .ph{height:105px}
.thumb .label{height:20px;background:#000;color:#fff;font-family:'Anton',sans-serif;font-size:12px;text-align:center;line-height:20px;letter-spacing:.4px}
.thumb .label em{font-style:normal;color:var(--blue)}

/* welcome */
.welcome-title{left:56px;top:632px;width:410px;text-align:center;font-family:'Anton',sans-serif;font-size:17px;color:#111}
.portrait{left:25px;top:680px;width:132px;height:132px;border-radius:50%;background:radial-gradient(circle at 50% 45%,#f1c6a4,#c78a5f 70%,#e4dccf);border:3px solid #fff;box-shadow:0 2px 6px rgba(0,0,0,.3)}
.welcome-text{left:186px;top:707px;width:308px;font-size:13px;line-height:18.5px;text-align:justify}
.sign{left:186px;top:800px;width:308px;text-align:right;font-size:13px;line-height:18.5px}

/* form */
.form{left:528px;top:627px;width:237px;height:255px;background:linear-gradient(#3a3a3a,#111);border-radius:3px}
.form-tab{left:571px;top:617px;width:144px;height:43px;background:var(--blue);color:#fff;font-size:12px;text-align:center;line-height:45px;box-shadow:0 3px 4px rgba(0,0,0,.4)}
.field{position:absolute;left:22px;width:189px;background:#4e4e4e;border-radius:4px;color:#cfcfcf;font-size:10px;padding:6px 12px}
.submit{left:589px;top:836px;width:114px;height:24px;background:linear-gradient(#f7b425,#d9900f);border-radius:4px;text-align:center;font-size:12px;line-height:24px;color:#222}

/* testimonials */
.testi{left:0;top:898px;width:785px;height:266px;background:var(--testi-bg)}
.testi-title{left:24px;top:925px;width:490px;display:flex;align-items:center;gap:12px;font-family:'Anton',sans-serif;font-size:17px;color:#111}
.testi-title::before,.testi-title::after{content:"";flex:1;height:2px;background:#111}
.avatar{left:215px;top:968px;width:82px;height:82px;border-radius:50%;border:3px solid var(--blue);background:radial-gradient(circle at 50% 45%,#f3d2b6,#c9a07b 70%,#eee)}
.quote{left:42px;top:1061px;width:457px;text-align:center;font-size:11.5px;line-height:18.5px;color:#333}
.quote b{color:var(--blue);font-weight:600}

.video{left:528px;top:921px;width:239px;height:193px;background:#fff;border:2px solid #222;box-shadow:0 8px 6px -4px rgba(0,0,0,.35)}
.video-head{height:29px;background:#111;color:var(--blue);font-family:'Anton',sans-serif;font-size:17px;text-align:center;line-height:30px}
.video-ph{position:absolute;left:3px;top:32px;width:229px;height:153px;background:linear-gradient(120deg,#d6b89d,#f2dcc6 45%,#caa88a 75%,#eee)}

/* footer */
.foot-line{left:0;top:1164px;width:785px;height:6px;background:var(--blue)}
.footer{left:0;top:1170px;width:785px;height:30px;background:var(--dark);color:#ddd;font-size:8px;padding:10px 29px;display:flex;justify-content:space-between}
</style>
</head>
<body>

<div class="abs topbar">
  <span class="item home">HOME</span>
  <span class="item lang">Language : &nbsp;<span>English (UK) &nbsp; | &nbsp; German</span></span>
  <span class="item help">Help</span>
</div>
<div class="abs search">Search . . .</div>

<div class="abs header"></div>
<div class="abs brand"><span class="mark"></span><span class="name">MARVELTRUST</span></div>
<svg class="abs phone-icon" width="20" height="30" viewBox="0 0 20 30" aria-hidden="true">
  <path d="M6 2 L11 4 L9 10 L6 10 Q5 15 6 20 L9 20 L11 26 L6 28 Q0 15 6 2Z" fill="#555"/>
</svg>
<div class="abs callout" style="left:378px">
  <div class="lead">Rufen Sie an für Beratung!</div>
  <div class="phone">301 - 480 - 7320</div>
</div>
<div class="abs socialbox"><i></i><i></i><i></i><i></i></div>
<div class="abs rule"></div>
<div class="abs band"></div>

<nav class="abs nav">
  <a style="width:157px">HOME</a>
  <a class="on" style="width:104px">ZAHNMEDIZIN ▾</a>
  <a style="width:104px">DENTALHYGIENE</a>
  <a style="width:80px">TEAM</a>
  <a style="width:80px">KONTAKT</a>
</nav>
<div class="abs dropdown">
  <div>Zahnarztbehandlung</div>
  <div class="on">Kompetenzen</div>
  <div>Zahnärztliche Behandlung</div>
  <div>Notfälle</div>
</div>

<div class="abs slider" role="img" aria-label="Bild eines lächelnden Mundes vor blauen Blüten"></div>
<div class="abs cap1">Gestalten Sie Ihr <em>Lächeln</em> heute und <em>Lächeln</em></div>
<div class="abs cap2">Mit neuer <em>Zuversicht</em></div>
<svg class="abs arrow" style="left:22px" width="24" height="46" viewBox="0 0 24 46" aria-hidden="true">
  <path d="M0 0 A23 23 0 0 1 0 46Z" fill="#111"/><path d="M7 15 L13 23 L7 31" stroke="#e8a317" stroke-width="2" fill="none"/>
</svg>
<svg class="abs arrow" style="left:743px" width="24" height="46" viewBox="0 0 24 46" aria-hidden="true">
  <path d="M24 0 A23 23 0 0 0 24 46Z" fill="#111"/><path d="M17 15 L11 23 L17 31" stroke="#e8a317" stroke-width="2" fill="none"/>
</svg>

<div class="abs thumb" style="left:56px">
  <div class="ph" role="img" aria-label="Bild von Zähnen vor und nach dem Aufhellen" style="background:linear-gradient(90deg,#d88a6c,#f0e2c8 50%,#f7f3ec 60%,#d98a70)"></div>
  <div class="label">WEIßE <em>FÜLLUNGEN</em></div>
</div>
<div class="abs thumb" style="left:290px">
  <div class="ph" role="img" aria-label="Bild einer lächelnden Frau mit grünem Apfel" style="background:linear-gradient(180deg,#e6c2a6,#f3e3d6 70%,#8dbb3c)"></div>
  <div class="label">DENTAL <em>HYGINE</em></div>
</div>
<div class="abs thumb" style="left:528px">
  <div class="ph" role="img" aria-label="Bild eines Mundes mit Zahnspiegel" style="background:linear-gradient(120deg,#f3dccd,#e39a80 50%,#f2f2f2)"></div>
  <div class="label">BRÜCKEN <em>UND</em> KRONEN</div>
</div>

<h1 class="abs welcome-title">Herzlich willkommen in unserer neuen Praxis.</h1>
<div class="abs portrait" role="img" aria-label="Porträtfoto der Zahnärztin"></div>
<p class="abs welcome-text">Es ist unser Ziel, Ihr Wohlbefinden zu steigern. Sie sollen die Schönheit des Alltags mit gesunden Zähnen geniessen und in jeder Situation herzhaft lachen können.</p>
<p class="abs sign">Ihre Zahnärztin<br>Dr. med. dent. Livia Marten-Seiler</p>

<div class="abs form">
  <div class="field" style="top:53px;height:27px">Name</div>
  <div class="field" style="top:84px;height:27px">Email</div>
  <div class="field" style="top:115px;height:83px">Nachricht</div>
</div>
<svg class="abs" style="left:563px;top:617px" width="160" height="10" viewBox="0 0 160 10" aria-hidden="true">
  <path d="M0 10 L8 0 L8 10Z M160 10 L152 0 L152 10Z" fill="#1b6f95"/>
</svg>
<div class="abs form-tab">Buchen Sie einen Termin</div>
<div class="abs submit">Einreichen</div>

<div class="abs testi"></div>
<h2 class="abs testi-title">TESIMONIALS</h2>
<div class="abs avatar" role="img" aria-label="Porträtfoto einer zufriedenen Patientin"></div>
<p class="abs quote">" Ich möchte Ihnen aus tiefstem Herzen danken, dass sie mir meine perfekte Lächeln und jüngeren Teint, hat mein Selbstvertrauen enorm gewachsen. Jas, sind Ihre Tal-ente endlos." - <b>Corinna</b></p>

<div class="abs video">
  <div class="video-head">VIDEO</div>
  <div class="video-ph" role="img" aria-label="Videovorschau einer lachenden Familie"></div>
  <svg class="abs" style="left:3px;top:164px" width="229" height="21" viewBox="0 0 229 21" aria-hidden="true">
    <rect width="229" height="21" fill="#ddd" opacity=".9"/>
    <rect x="6" y="6" width="20" height="9" rx="4" fill="#888"/>
    <rect x="32" y="8" width="170" height="5" rx="2" fill="#333"/>
    <rect x="32" y="8" width="105" height="5" rx="2" fill="#d11"/>
    <circle cx="137" cy="10.5" r="4" fill="#eee" stroke="#999"/>
    <path d="M210 7 L214 7 L218 4 L218 17 L214 14 L210 14Z" fill="#777"/>
  </svg>
  <svg class="abs" style="left:210px;top:110px" width="16" height="52" viewBox="0 0 16 52" aria-hidden="true">
    <rect x="2" y="0" width="12" height="52" rx="6" fill="#ddd" stroke="#999"/>
    <rect x="6" y="18" width="4" height="30" rx="2" fill="#2494c4"/>
    <rect x="6" y="4" width="4" height="14" rx="2" fill="#333"/>
  </svg>
</div>

<div class="abs foot-line"></div>
<svg class="abs" style="left:396px;top:1170px" width="16" height="8" viewBox="0 0 16 8" aria-hidden="true"><path d="M0 0 L16 0 L8 8Z" fill="#3cb3e0"/></svg>
<footer class="abs footer">
  <span>Home &nbsp;|&nbsp; Zahnmedizin &nbsp;|&nbsp; Dentalhygiene &nbsp;|&nbsp; Team &nbsp;|&nbsp; Kontakt</span>
  <span>2014 www.pelbrika-example.ch</span>
</footer>

</body>
</html>
```